Wordpress Layout, Plug-in, Mash-up Overhaul

We have collection of vertical topic portals; in each portal, a post typically is an article which goes with a subject video, following are 5 reference sites:

http://www.ledgerbrook.com/
http://www.velmacounsel.com/
http://www.shimmerlane.tv/
http://www.nestharbor.com/
http://www.ladiestalkly.com/

We obtained most of our based WP theme from various premium WP template membership sites, subsequently re-organise, mash-up content to produce sites as above; however we start to be constraint as we get into a fixed pattern of laying out our contents and we seeking professional help to re-work this. these re-work can includes as follows.

1. proposal on creative re-placement of component / re-layout on the templates. Should also suggest different way for the advertising banner placement etc.

2. proposal on right and appropriate use of WP plugins (paid or free but have to be secured and reliable) to achieve more relevant add-on of content where necessary (rss, etc)

Objective:
We want to move away from our internal team design constraint and also moving alway from being stuck with certain stereo-type way of WP content site. However the proposed WP design should still be a portal-centric type vs blogging/product-centric.

Deliverables:
1. We don't need the actual cut template but a design mockup of the home page and relevant sub pages (.psd, jpg etc) for the proposed re-design. Based on the above 5 listed sites, the deliverable would be at least 10 pages of design layout work (considering home page and 1 sub pages for each domain; could be more if necessary)

2. The plugins reference where necessary

What's expected from your proposal for the bid:
We would like a mockup of a re-design from any pick from any of the above 5 domains

```html
<!DOCTYPE html>
<html lang="en">
<head>
<meta charset="utf-8">
<title>Velma Counsel — Home</title>
<link href="https://fonts.googleapis.com/css2?family=Lato:wght@400;700;900&family=Open+Sans:wght@400;600;700&display=swap" rel="stylesheet">
<style>
:root{
  --magenta:#a5329c;
  --magenta-deep:#7d2a86;
  --caption:rgba(122,38,134,.86);
  --ink:#2e2e30;
  --muted:#555;
  --topbar:#ececee;
  --gray-band:#8a8a8c;
  --light-band:#eeeef0;
  --footer:#505053;
  --footer-base:#3e3e40;
  --white:#fff;
}
*{margin:0;padding:0;box-sizing:border-box}
html,body{width:1200px;height:3025px;overflow:hidden}
body{font-family:"Open Sans",Arial,sans-serif;color:var(--ink);background:var(--white);position:relative}
.abs{position:absolute}
.ph{position:absolute;display:block}
h2.section-title{font-family:"Lato",Arial,sans-serif;font-weight:900;font-size:28px;color:var(--magenta);text-transform:uppercase;position:absolute}

/* top bar */
.topbar{top:0;left:0;width:1200px;height:28px;background:var(--topbar);font-size:10px;color:#555}
.topbar .links{position:absolute;left:182px;top:8px;display:flex;gap:8px}
.topbar .links span::after{content:"|";margin-left:8px;color:#aaa}
.topbar .links span:last-child::after{content:""}
.topbar .contact{position:absolute;right:182px;top:8px;display:flex;gap:18px;align-items:center}
.topbar .contact i{display:inline-block;width:8px;height:8px;background:var(--magenta);border-radius:2px;margin-right:6px;vertical-align:-1px}

/* header */
.header{top:28px;left:0;width:1200px;height:66px;background:var(--white)}
.logo{position:absolute;left:182px;top:16px;display:flex;align-items:center;gap:8px;font-family:"Lato",sans-serif;font-weight:900;font-size:20px;color:var(--magenta)}
.logo .dot{width:26px;height:26px;border-radius:50%;background:var(--magenta)}
.mainnav{position:absolute;left:424px;top:26px;display:flex;gap:22px;font-family:"Lato",sans-serif;font-weight:700;font-size:11.5px;color:#333;text-transform:uppercase}
.mainnav .active{color:var(--magenta)}

/* hero */
.hero{top:94px;left:0;width:1200px;height:354px;background:linear-gradient(180deg,#c86bc9 0%,#d774d4 40%,#b64db6 62%,#8e2f93 100%)}
.hero .title{position:absolute;left:182px;top:232px;font-family:"Lato",sans-serif;font-weight:900;font-size:27px;color:#fff;text-transform:uppercase}
.hero .sub{position:absolute;left:182px;top:264px;width:480px;font-family:"Lato",sans-serif;font-weight:700;font-size:14px;line-height:18px;color:#fff}
.arrow{position:absolute;top:280px;width:50px;height:50px;border-radius:50%;background:rgba(213,94,180,.85)}
.arrow svg{position:absolute;left:17px;top:15px}

/* latest news */
.newsbar{top:452px;left:0;width:1200px;height:44px;background:#fff;font-size:10px;color:#444}
.newsbar .tag{position:absolute;left:0;top:0;height:44px;width:290px;background:var(--magenta);clip-path:polygon(0 0,100% 0,88% 100%,0 100%)}
.newsbar .tag span{position:absolute;left:182px;top:14px;font-family:"Lato",sans-serif;font-weight:900;color:#fff;font-size:10px}
.newsbar .items{position:absolute;left:292px;top:15px;display:flex;gap:14px;white-space:nowrap}
.newsbar .items span::after{content:"|";margin-left:14px;color:#aaa}

/* featured grid */
.featured{top:496px;left:0;width:1200px;height:628px;background:linear-gradient(180deg,#9a9a9c,#6e6e70 55%,#8e8e90)}
.tile{position:absolute;overflow:hidden}
.tile .caption{position:absolute;background:var(--caption);color:#fff;text-align:center;padding:8px 10px}
.tile .caption h3{font-family:"Lato",sans-serif;font-weight:900;font-size:12.5px;text-transform:uppercase;margin-bottom:4px}
.tile .caption p{font-size:10px;line-height:12px}
.refresh{position:absolute;display:flex;gap:12px}

/* recent posts */
.recent-lead-name,.widget-name{font-family:"Lato",sans-serif;font-weight:900;font-size:20px;color:#2b2b2b;position:absolute}
.lead-text{position:absolute;font-size:14px;line-height:17px;color:#444}
.mini{position:absolute;left:668px;width:360px;height:70px}
.mini .thumb{position:absolute;left:0;top:0;width:106px;height:68px}
.mini h4{position:absolute;left:118px;top:6px;font-family:"Lato",sans-serif;font-weight:900;font-size:16px;color:#2b2b2b}
.mini p{position:absolute;left:118px;top:28px;width:220px;font-size:11px;line-height:13px;color:#444}

/* carousel */
.carousel{top:1624px;left:0;width:1200px;height:268px;background:linear-gradient(180deg,#7b7b7d,#9b9b9d 60%,#b6b6b8)}
.carousel h2{position:absolute;left:0;width:1200px;top:34px;text-align:center;font-family:"Lato",sans-serif;font-weight:900;font-size:25px;color:#fff}
.citem{position:absolute;top:76px;width:192px}
.citem .img{width:192px;height:128px}
.citem p{margin-top:6px;text-align:center;font-size:13px;line-height:15px;color:#fff}

/* widgets */
.widgets{top:1892px;left:0;width:1200px;height:726px;background:var(--light-band)}
.tabs{position:absolute;left:182px;top:2000px;display:flex;gap:28px;font-family:"Lato",sans-serif;font-weight:700;font-size:14px;color:#333}
.tabs .on{color:var(--magenta)}
.small-card{position:absolute;top:2384px;width:191px}
.small-card .img{width:191px;height:128px}
.small-card h5{font-family:"Lato",sans-serif;font-weight:900;font-size:16px;margin-top:20px}
.small-card p{font-size:10.5px;line-height:13px;color:#444}
.catlist{position:absolute;left:787px;top:2023px;width:230px;background:#fff;border:1px solid #ddd}
.catlist li{list-style:none;height:54.5px;border-bottom:1px solid #ddd;display:flex;align-items:center;padding-left:14px;font-family:"Lato",sans-serif;font-weight:700;font-size:13px;color:#333}
.catlist li:last-child{border-bottom:0}
.catlist li b{color:var(--magenta);margin-right:16px;font-size:11px}
.promo{position:absolute;left:787px;top:2423px;width:230px;height:151px;background:linear-gradient(180deg,#6cb6e4,#a9d7ef 55%,#e7dcc0)}
.promo .head{position:absolute;left:12px;top:14px;font-family:"Lato",sans-serif;font-weight:900;font-size:17px;line-height:18px;color:#fff;text-transform:uppercase}
.promo .cta{position:absolute;left:0;bottom:0;width:100%;height:30px;background:#1f1f21;color:#fff;font-family:"Lato",sans-serif;font-weight:900;font-size:13px;padding:7px 12px}

/* footer */
.footer{top:2618px;left:0;width:1200px;height:339px;background:var(--footer);color:#fff}
.footer h6{position:absolute;font-family:"Lato",sans-serif;font-weight:900;font-size:14px;text-transform:uppercase;color:#fff}
.select{position:absolute;left:182px;top:2692px;width:254px;height:44px;background:#fff;color:#888;font-size:13px;padding:13px 14px}
.select svg{position:absolute;right:14px;top:18px}
.social{position:absolute;left:182px;top:2810px;display:flex;gap:6px}
.social span{width:50px;height:50px;display:block}
.fthumb{position:absolute;width:111px;height:71px}
.welcome{position:absolute;left:744px;top:2684px;width:272px;font-size:12px;line-height:19.5px;color:#eee}
.basebar{top:2957px;left:0;width:1200px;height:68px;background:var(--footer-base);color:#eee;font-size:11.5px;text-align:center;padding-top:17px;line-height:19px}
</style>
</head>
<body>

<div class="abs topbar">
  <div class="links"><span>Home</span><span>About Us</span><span>Advertise with Us</span><span>Privacy Policy</span><span>Contact Us</span><span>Sitemap</span></div>
  <div class="contact"><span><i></i>0000 000 00 00</span><span><i></i>desk@velmacounsel.com</span></div>
</div>

<header class="abs header">
  <div class="logo"><span class="dot"></span>Velma Counsel</div>
  <nav class="mainnav">
    <span class="active">Cheap Steals</span><span>Hair &amp; Makeup</span><span>Health &amp; Fitness</span><span>Love &amp; Relationships</span><span>Skincare</span><span>Travel</span><span>What's Hot</span>
  </nav>
</header>

<section class="abs hero" role="img" aria-label="Silhouette of a couple leaping on a beach at sunset in magenta tones">
  <div class="arrow" style="left:108px"><svg width="16" height="20" viewBox="0 0 16 20"><path d="M12 2 L4 10 L12 18" stroke="#fff" stroke-width="2.5" fill="none"/></svg></div>
  <div class="arrow" style="left:1042px"><svg width="16" height="20" viewBox="0 0 16 20"><path d="M4 2 L12 10 L4 18" stroke="#fff" stroke-width="2.5" fill="none"/></svg></div>
</section>
<div class="hero-text">
  <div class="abs" style="left:182px;top:232px;font-family:'Lato',sans-serif;font-weight:900;font-size:27px;color:#fff">BALANCING WORK AND FAMILY</div>
  <div class="abs" style="left:182px;top:264px;width:480px;font-family:'Lato',sans-serif;font-weight:700;font-size:14px;line-height:18px;color:#fff">Kissing is one of the most amazing and enjoyable things that you and your partner can get into when having</div>
</div>

<div class="abs newsbar">
  <div class="tag"><span>LATEST NEWS</span></div>
  <div class="items"><span>How to Wear Cocktail Dresses 7:08 am</span><span>How to Layer Clothes 7:08 am</span><span>Savvy Jewelry Shopping Tips 7:08 am</span><span>How to Layer Clothes 7:08 am</span><span style="">Savvy Jewelry Shopping Tips 7:08 am</span></div>
</div>

<section class="abs featured" role="img" aria-label="Muted grey beach scene as section backdrop"></section>
<div class="refresh" style="left:976px;top:520px">
  <svg width="14" height="14" viewBox="0 0 14 14"><path d="M11 4 A5 5 0 1 0 12 8" stroke="#fff" stroke-width="2" fill="none"/><path d="M9 1 L12 4 L8 5Z" fill="#fff"/></svg>
  <svg width="14" height="14" viewBox="0 0 14 14"><circle cx="2.5" cy="11.5" r="1.8" fill="#fff"/><path d="M1 6 A7 7 0 0 1 8 13 M1 1.5 A11.5 11.5 0 0 1 12.5 13" stroke="#fff" stroke-width="2" fill="none"/></svg>
</div>
<article class="tile" style="left:182px;top:549px;width:548px;height:294px">
  <div class="ph" style="inset:0;background:linear-gradient(120deg,#c8a48a,#e7c9b3 45%,#8a6a56)" role="img" aria-label="Makeup artist applying makeup to a model"></div>
  <div class="caption" style="left:16px;top:202px;width:500px;height:80px;text-align:left">
    <h3>Spring Catwalk Makeup Tutorial</h3>
    <p>Fresh, clear, and dewy makeup has been all over the catwalks this spring and summer. The look is delicate and natural, with just a touch of illumination; it's quite the reverse</p>
  </div>
</article>
<article class="tile" style="left:756px;top:549px;width:261px;height:294px">
  <div class="ph" style="inset:0;background:linear-gradient(135deg,#e9d8cd,#d7b9a6 50%,#b9a2c4)" role="img" aria-label="Woman with eyeshadow palette and brushes"></div>
  <div class="caption" style="left:14px;top:182px;width:233px;height:100px">
    <h3>How To Do Artistic Makeup</h3>
    <p>When it comes to applying makeup, some people are very adept at this skill while others struggle with the entire concept. Applying artistic makeup is a great way to completely transform</p>
  </div>
</article>
<article class="tile" style="left:182px;top:863px;width:262px;height:240px">
  <div class="ph" style="inset:0;background:linear-gradient(160deg,#7a4a86,#5a3a3e 60%,#3b2a30)" role="img" aria-label="Woman wearing purple evening makeup"></div>
  <div class="caption" style="left:14px;top:130px;width:234px;height:98px">
    <h3>Date Night Makeup Tutorial</h3>
    <p>Date night is always fun, but let's face it, it may necessitate a lot of prep time. Often, women getting ready for a date don't know how they should do their</p>
  </div>
</article>
<article class="tile" style="left:470px;top:863px;width:260px;height:240px">
  <div class="ph" style="inset:0;background:linear-gradient(160deg,#d9c2b2,#b99882 60%,#8e7262)" role="img" aria-label="Close portrait of a woman with bold eye makeup"></div>
  <div class="caption" style="left:14px;top:130px;width:232px;height:98px">
    <h3>Makeup Dos and Donts</h3>
    <p>You always want to look your best when wearing make-up, and to do so you need to make the correct choice in product as well as learning the right techniques.</p>
  </div>
</article>
<article class="tile" style="left:756px;top:863px;width:261px;height:240px">
  <div class="ph" style="inset:0;background:linear-gradient(160deg,#a0705a,#6e4436 60%,#d8c4b8)" role="img" aria-label="Woman with summer evening makeup and wavy hair"></div>
  <div class="caption" style="left:14px;top:130px;width:233px;height:98px">
    <h3>Summer Evening Makeup Look</h3>
    <p>Dramatic Summer Time Looks Summer is a great time to play with your makeup. This is an easy, breezy time of year...</p>
  </div>
</article>

<h2 class="section-title" style="left:178px;top:1154px">Recent Posts</h2>
<div class="refresh" style="left:976px;top:1164px">
  <svg width="14" height="14" viewBox="0 0 14 14"><path d="M11 4 A5 5 0 1 0 12 8" stroke="#444" stroke-width="2" fill="none"/><path d="M9 1 L12 4 L8 5Z" fill="#444"/></svg>
  <svg width="14" height="14" viewBox="0 0 14 14"><circle cx="2.5" cy="11.5" r="1.8" fill="#444"/><path d="M1 6 A7 7 0 0 1 8 13 M1 1.5 A11.5 11.5 0 0 1 12.5 13" stroke="#444" stroke-width="2" fill="none"/></svg>
</div>
<div class="ph" style="left:182px;top:1206px;width:447px;height:283px;background:linear-gradient(180deg,#2c8fd0,#5cb8dc 45%,#1d9ba6 70%,#0f6e86)" role="img" aria-label="Woman on a boat raising her arms towards a tropical island"></div>
<div class="recent-lead-name" style="left:180px;top:1500px">NAME NAME</div>
<p class="lead-text" style="left:182px;top:1526px;width:420px">Lorem Ipsum is simply dummy text of the printing and typesetting industry. Lorem Ipsum is simply dummy text of the printing and typesetting industry.</p>

<div class="mini" style="top:1206px"><div class="thumb" style="background:linear-gradient(135deg,#cfd8e0,#8fa0ae)" role="img" aria-label="Couple sitting together outdoors"></div><h4>NAME NAME</h4><p>Lorem Ipsum is simply dummy text of the printing and typesetting industry.</p></div>
<div class="mini" style="top:1285px"><div class="thumb" style="background:linear-gradient(135deg,#6a4a3e,#c49a84)" role="img" aria-label="Couple about to kiss"></div><h4>NAME NAME</h4><p>Lorem Ipsum is simply dummy text of the printing and typesetting industry.</p></div>
<div class="mini" style="top:1364px"><div class="thumb" style="background:linear-gradient(135deg,#b06e3c,#e8c090)" role="img" aria-label="Smiling couple close together"></div><h4>NAME NAME</h4><p>Lorem Ipsum is simply dummy text of the printing and typesetting industry.</p></div>
<div class="mini" style="top:1443px"><div class="thumb" style="background:linear-gradient(135deg,#8a5a44,#d8b49a)" role="img" aria-label="Couple relaxing on a sofa"></div><h4>NAME NAME</h4><p>Lorem Ipsum is simply dummy text of the printing and typesetting industry.</p></div>
<div class="mini" style="top:1522px"><div class="thumb" style="background:linear-gradient(135deg,#e4e4e6,#a6a8ae)" role="img" aria-label="Couple sitting back to back"></div><h4>NAME NAME</h4><p>Lorem Ipsum is simply dummy text of the printing and typesetting industry.</p></div>

<section class="abs carousel" role="img" aria-label="Muted grey beach backdrop with a deck chair">
  <h2>CAROUSEL</h2>
  <svg class="abs" style="left:980px;top:46px" width="14" height="14" viewBox="0 0 14 14"><circle cx="2.5" cy="11.5" r="1.8" fill="#fff"/><path d="M1 6 A7 7 0 0 1 8 13 M1 1.5 A11.5 11.5 0 0 1 12.5 13" stroke="#fff" stroke-width="2" fill="none"/></svg>
  <div class="citem" style="left:204px"><div class="img" style="background:linear-gradient(135deg,#8a6a50,#d4b890)" role="img" aria-label="Friends laughing at a cafe table"></div><p>How To Survive A Break Uptypesetting industry.</p></div>
  <div class="citem" style="left:405px"><div class="img" style="background:linear-gradient(135deg,#c8c8d0,#7a8ab0)" role="img" aria-label="Group of women with shopping bags"></div><p>How To Make Public Displays Of Affection</p></div>
  <div class="citem" style="left:606px"><div class="img" style="background:linear-gradient(180deg,#7ab0e0,#c9a880)" role="img" aria-label="Women giving thumbs up in a European city"></div><p>How To Be Romantic</p></div>
  <div class="citem" style="left:806px"><div class="img" style="background:linear-gradient(135deg,#5a8a4a,#d46a6a)" role="img" aria-label="Women walking outdoors with bags"></div><p>Balancing Work and Family</p></div>
</section>

<section class="abs widgets"></section>
<h2 class="section-title" style="left:178px;top:1934px">Widget Tabs</h2>
<div class="tabs"><span>POPULAR</span><span class="on">RECENT</span><span>TAGS</span></div>
<div class="ph" style="left:182px;top:2025px;width:591px;height:265px;background:linear-gradient(180deg,#f4f4f6,#dcdce0 70%,#bcbcc2)" role="img" aria-label="Couple sitting back to back on a white sofa"></div>
<div class="widget-name" style="left:180px;top:2302px">NAME NAME</div>
<p class="lead-text" style="left:182px;top:2328px;width:590px;font-size:13px;line-height:16px">Lorem Ipsum is simply dummy text of the printing and typesetting industry. Lorem Ipsum is simply dummy text of the printing and typesetting industry.</p>
<div class="small-card" style="left:182px"><div class="img" style="background:linear-gradient(135deg,#f3ece6,#c49478)" role="img" aria-label="Portrait of a woman with green makeup"></div><h5>NAME NAME</h5><p>Lorem Ipsum is simply dummy text of the printing and typesetting industry.</p></div>
<div class="small-card" style="left:382px"><div class="img" style="background:linear-gradient(135deg,#6a5046,#caa08a)" role="img" aria-label="Close portrait of a woman's eyes"></div><h5>NAME NAME</h5><p>Lorem Ipsum is simply dummy text of the printing and typesetting industry.</p></div>
<div class="small-card" style="left:582px"><div class="img" style="background:linear-gradient(135deg,#d8d0cc,#8a7066)" role="img" aria-label="Woman applying makeup with a brush"></div><h5>NAME NAME</h5><p>Lorem Ipsum is simply dummy text of the printing and typesetting industry.</p></div>

<h2 class="section-title" style="left:787px;top:1934px">Categories</h2>
<ul class="catlist">
  <li><b>&gt;&gt;</b>CHEAP STEALS</li>
  <li><b>&gt;&gt;</b>HAIR &amp; MAKEUP</li>
  <li><b>&gt;&gt;</b>HEALTH &amp; FITNESS</li>
  <li><b>&gt;&gt;</b>LOVE &amp; RELATIONSHIPS</li>
  <li><b>&gt;&gt;</b>SKINCARE</li>
  <li><b>&gt;&gt;</b>TRAVEL</li>
  <li><b>&gt;&gt;</b>WHAT'S HOT</li>
</ul>
<div class="promo" role="img" aria-label="Beach with umbrella and deck chairs travel advert">
  <div class="head">Craving<br>for travel</div>
  <div class="cta">CLICK HERE</div>
</div>

<footer class="abs footer"></footer>
<h6 class="abs" style="left:182px;top:2656px;font-family:'Lato',sans-serif;font-weight:900;font-size:14px;color:#fff">NAVIGATION</h6>
<div class="select">SELECT CATEGORY<svg width="12" height="7" viewBox="0 0 12 7"><path d="M0 0 H12 L6 7Z" fill="#555"/></svg></div>
<h6 class="abs" style="left:182px;top:2770px;font-family:'Lato',sans-serif;font-weight:900;font-size:14px;color:#fff">CONNECT WITH VELMA COUNSEL</h6>
<div class="social"><span style="background:#3b5998"></span><span style="background:#cb2027"></span><span style="background:#f7931e"></span></div>
<h6 class="abs" style="left:472px;top:2656px;font-family:'Lato',sans-serif;font-weight:900;font-size:14px;color:#fff">LATEST POST IMAGES</h6>
<div class="fthumb" style="left:472px;top:2690px;background:linear-gradient(135deg,#e0a0b8,#b86a8a)" role="img" aria-label="Women smiling together"></div>
<div class="fthumb" style="left:594px;top:2690px;background:linear-gradient(135deg,#8a7a6a,#d0b8a0)" role="img" aria-label="Friends in a group"></div>
<div class="fthumb" style="left:472px;top:2775px;background:linear-gradient(135deg,#c04a3a,#e8a07a)" role="img" aria-label="Fitness class stretching"></div>
<div class="fthumb" style="left:594px;top:2775px;background:linear-gradient(135deg,#6a9a5a,#c8d0a0)" role="img" aria-label="Women exercising outdoors"></div>
<div class="fthumb" style="left:472px;top:2860px;background:linear-gradient(135deg,#e8c070,#d08a50)" role="img" aria-label="Group laughing in the sun"></div>
<div class="fthumb" style="left:594px;top:2860px;background:linear-gradient(135deg,#7aa8d8,#e0c8b0)" role="img" aria-label="Smiling couple outdoors"></div>
<h6 class="abs" style="left:744px;top:2656px;font-family:'Lato',sans-serif;font-weight:900;font-size:14px;color:#fff">WELCOME</h6>
<p class="welcome">Velma Counsel is another breakthrough forum for all fitness and health enthusiasts out there. Of course, this website is specifically designed for women. In this day and age, staying fit and healthy has become a goal in many women's lives. To help you in reaching your goal, Velma Counsel brings to you some healthy tips, exercise suggestions, easy diet plans, and blogposts with secret tips for diet and weight loss. This women's health and fitness website is designed to reach that niche of all new generation women who wants to stay healthy and fit in this stressful and busy world.</p>

<div class="abs basebar">Email us <b>help@velmacounsel.com</b> | Call us <b>000-000-0000</b> | Visit us <b>www.velmacounsel.com</b><br>© 2014 Velma Counsel | All rights reserved</div>

</body>
</html>
```